Commercial brochure presenting independent commercial activity

I would like to create a commercial brochure for my new professional activity.

This is a personal and not business oriented brochure because I will become an independent project assistant to assist engineering offices with one-off missions.

I want a 4 page A4 brochure

• Page 1: Logo, personal photo
• Page 2 and 3: Personal presentation and presentation of my activities
• Page4: contact information

My target audience: engineering offices and design offices

The objective of the brochure: it is to make my profile interesting so that design offices will want to use my services when there is demand

Sector of activity: food, chemical, pharmaceutical industry
The text of the brochure must remain in French and contain what is in the attached file

On page 1, you must keep a space for a photo of my profile which I will insert later because I do not have it yet and insert my monogram (it can be reworked to be inserted in the brochure)
The image with the logo (R/M) is the color range I want

Target Market(s)

engineering offices and design offices

Industry/Entity Type

industrie alimentaire, chimique, pharmaceutique

Font styles to use
Sans Serif

Colors
0094D4
00A9DD
6FCCEA
C7EBF8
E9F6FB

Requirements
Must have
• The plate must comply with current codes. Each reader must think that I am dynamic and that my services are of quality and equivalent to the presentation

```html
<!DOCTYPE html>
<html lang="fr">
<head>
<meta charset="utf-8">
<title>Rémi Marchand – Brochure</title>
<link href="https://fonts.googleapis.com/css2?family=Mulish:wght@400;600;700;800;900&family=Marcellus&display=swap" rel="stylesheet">
<style>
  :root{
    --bg:#54504d;
    --blue-deep:#0094d4;
    --blue:#00a9dd;
    --blue-mid:#4fb3d3;
    --blue-light:#6fccea;
    --blue-pale:#c7ebf8;
    --blue-mist:#e9f6fb;
    --navy:#1f5fa8;
    --cream:#eef1d2;
    --ink:#2b3440;
    --white:#ffffff;
  }
  *{margin:0;padding:0;box-sizing:border-box}
  html,body{width:1200px;height:1200px;overflow:hidden;background:var(--bg);font-family:"Mulish",sans-serif}
  .canvas{position:relative;width:1200px;height:1200px}

  /* Cover sheet (front + back, printed sideways) */
  .cover{position:absolute;left:55px;top:310px;width:437px;height:617px;overflow:hidden;
    background:linear-gradient(160deg,var(--blue-pale) 0%,var(--cream) 35%,var(--cream) 62%,var(--blue-pale) 88%,var(--blue-light) 100%)}
  .cover__fold{position:absolute;left:0;right:0;top:308px;height:1px;background:rgba(0,0,0,.06)}
  .cover__photo{position:absolute;left:150px;top:70px;width:287px;height:160px;
    background:linear-gradient(90deg,#f4f7f8,#ffffff);border-radius:80px 0 0 60px}
  .vtext{position:absolute;writing-mode:vertical-rl;transform:rotate(180deg);white-space:nowrap}
  .cover__photo-label{left:380px;top:138px;font-family:"Marcellus",serif;color:var(--navy);font-size:11px;font-weight:700}
  .brand{font-family:"Marcellus",serif;color:var(--blue-deep)}
  .mark{position:absolute;border-radius:50%;background:var(--blue-deep)}
  .cover__mark{left:36px;top:128px;width:34px;height:34px}
  .cover__name{left:98px;top:82px;font-size:17px}
  .cover__role{left:120px;top:104px;font-size:7px;color:var(--blue-deep);font-family:"Marcellus",serif}
  .back__mark{left:248px;top:452px;width:26px;height:26px}
  .back__name{left:288px;top:415px;font-size:11px}
  .back__role{left:304px;top:440px;font-size:5px;font-family:"Marcellus",serif;color:var(--blue-deep)}
  .back__contact{left:330px;top:425px;font-family:"Marcellus",serif;font-size:8px;line-height:11px;color:var(--navy);font-style:normal}
  .back__contact strong{font-size:9px}

  /* Inside spread */
  .spread{position:absolute;left:536px;top:430px;width:618px;height:434px;background:var(--white);overflow:hidden;color:var(--white)}
  .spread__shape{position:absolute;inset:0}
  .spread__fold{position:absolute;left:309px;top:0;bottom:0;width:1px;background:rgba(0,0,0,.07)}
  .block{position:absolute}
  .lead-title{left:38px;top:38px;width:210px;font-weight:900;font-size:13px;line-height:16px;color:var(--navy)}
  .lead-title span{color:var(--white)}
  .lead-text{left:38px;top:94px;width:234px;font-size:7px;font-weight:700;line-height:8.2px}
  .section-title{font-weight:900;font-size:10.5px;color:var(--navy);border-bottom:1px solid var(--white);padding-bottom:2px;display:inline-block}
  .expertise-title{left:38px;top:155px}
  .skill{position:absolute;width:120px}
  .skill__icon{position:absolute;left:0;top:0;width:18px;height:18px;border-radius:50%;background:var(--white);border:1.5px solid var(--blue-pale)}
  .skill__icon::after{content:"";position:absolute;left:5px;top:5px;width:6px;height:6px;border:1.2px solid var(--blue-mid);border-radius:2px}
  .skill__title{margin-left:23px;font-weight:800;font-size:7.5px;line-height:9px;color:var(--navy)}
  .skill ul{list-style:none;margin:3px 0 0 23px;font-size:5.6px;line-height:7px;font-weight:600}
  .skill li{position:relative;padding-left:6px}
  .skill li::before{content:"";position:absolute;left:0;top:2.3px;width:3px;height:3px;border-radius:50%;background:var(--navy)}

  .advantage-title{left:345px;top:44px;border-bottom-color:var(--blue-deep)}
  .adv{position:absolute;left:315px;width:288px;padding:5px 10px 5px 60px;color:var(--ink)}
  .adv--tint{background:linear-gradient(90deg,rgba(199,235,248,.35),var(--blue-mist));border-radius:0 20px 20px 0}
  .adv__title{font-weight:800;font-size:7.5px;line-height:9px;color:var(--navy)}
  .adv__text{font-size:5.6px;line-height:6.8px;margin-top:3px}
  .adv__icon{position:absolute;left:32px;top:5px;width:18px;height:18px;border-radius:50%;background:var(--navy)}
  .adv__icon svg{position:absolute;left:4px;top:4px}
  .band-mark{left:510px;top:350px;width:24px;height:24px}
  .band-name{left:430px;width:188px;top:400px;text-align:center;font-family:"Marcellus",serif;font-size:11px;color:var(--white)}
  .band-role{left:430px;width:188px;top:416px;text-align:center;font-family:"Marcellus",serif;font-size:5.5px;color:var(--blue-mist)}
</style>
</head>
<body>
<main class="canvas">

  <section class="cover" aria-label="Couverture et dos de la brochure">
    <div class="cover__fold"></div>
    <div class="cover__photo" role="img" aria-label="Emplacement réservé pour la photo de profil"></div>
    <p class="vtext cover__photo-label">Your photo</p>
    <div class="mark cover__mark"></div>
    <p class="vtext brand cover__name">Rémi Marchand</p>
    <p class="vtext cover__role">Assistant de projet indépendant</p>

    <div class="mark back__mark"></div>
    <p class="vtext brand back__name">Rémi Marchand</p>
    <p class="vtext back__role">Assistant de projet indépendant</p>
    <address class="vtext back__contact">
      <strong>ch. des Érables 8</strong><br>
      ⌖ 1870 Monthey<br>
      ✉ remi@marchand-projets.ch<br>
      ☏ +41 78 512 34 56
    </address>
  </section>

  <section class="spread" aria-label="Pages intérieures">
    <svg class="spread__shape" width="618" height="434" viewBox="0 0 618 434" aria-hidden="true">
      <defs>
        <linearGradient id="blueFill" x1="0" y1="0" x2="1" y2="1">
          <stop offset="0" stop-color="#3ea6cd"/>
          <stop offset="1" stop-color="#4cb6d9"/>
        </linearGradient>
      </defs>
      <path d="M0,0 H270 C305,30 318,110 312,200 C306,300 400,380 500,390 L618,390 V434 H215 C120,420 30,350 0,262 Z" fill="url(#blueFill)"/>
    </svg>
    <div class="spread__fold"></div>

    <h1 class="block lead-title">Rémi Marchand :<br><span>Un atout précieux pour votre bureau d'études</span></h1>
    <p class="block lead-text">Avec plus de 30 ans d'expérience dans l'industrie, je suis un expert chevronné en conception, gestion de projets et sécurité. J'offre mes services d'assistant de projet indépendant pour vous aider à gérer les pics de charge et les besoins spécifiques de votre bureau d'études.</p>

    <h2 class="block section-title expertise-title">Mon expertise :</h2>

    <div class="skill" style="left:38px;top:182px">
      <span class="skill__icon"></span>
      <p class="skill__title">Conception &amp; Design :</p>
      <ul><li>Maquettes 3D (logiciel CAO 3D)</li><li>Plans, schémas, RI/P&amp;ID, Flowsheets</li><li>Spécifications, catalogues, définition des fournitures</li></ul>
    </div>
    <div class="skill" style="left:38px;top:247px">
      <span class="skill__icon"></span>
      <p class="skill__title">Gestion de Projets :</p>
      <ul><li>Rédaction d'appels d'offre</li><li>Préparation de budgets</li><li>Réalisation de plannings</li><li>Estimations budgétaires</li><li>Réponse aux appels d'offre</li></ul>
    </div>
    <div class="skill" style="left:38px;top:320px">
      <span class="skill__icon"></span>
      <p class="skill__title">Sécurité :</p>
      <ul><li>Sécurité machine</li><li>Plans de montage</li><li>Edition de PHS</li></ul>
    </div>
    <div class="skill" style="left:178px;top:182px;width:100px">
      <span class="skill__icon"></span>
      <p class="skill__title">Documentation Technique :</p>
      <ul><li>DESP</li><li>Documentations spécifiques</li></ul>
    </div>
    <div class="skill" style="left:178px;top:250px;width:100px">
      <span class="skill__icon"></span>
      <p class="skill__title">Expertise :</p>
      <ul><li>Ma connaissance approfondie de la métallurgie (tuyauterie, serrurerie, chaudronnerie, charpente métallique, montage) me permet de garantir des études complètes et d'éviter les oublis.</li></ul>
    </div>

    <h2 class="block section-title advantage-title">Votre avantage :</h2>

    <div class="adv" style="top:63px">
      <span class="adv__icon"><svg width="10" height="10" viewBox="0 0 10 10"><path d="M1,5 H3 V9 H1 Z M3.5,5 L5.5,1 C6.5,1 6.5,2 6.2,3.5 H9 L8,9 H3.5 Z" fill="#fff"/></svg></span>
      <p class="adv__title">Connaissance des besoins des concepteurs et des fabricants :</p>
      <p class="adv__text">J'ai travaillé des deux côtés, ce qui me permet de comprendre les défis et les attentes de chacun.</p>
    </div>
    <div class="adv adv--tint" style="top:108px">
      <p class="adv__title">Flexibilité :</p>
      <p class="adv__text">Je suis disponible pour des missions ponctuelles et à durée déterminée, sans engagement à long terme.</p>
    </div>
    <div class="adv" style="top:148px">
      <p class="adv__title">Efficacité :</p>
      <p class="adv__text">Je peux vous aider à gérer les surcharges de travail et à respecter vos délais.</p>
    </div>
    <div class="adv adv--tint" style="top:187px">
      <p class="adv__title">Collaboration fluide :</p>
      <p class="adv__text">Je suis à votre disposition pour discuter de vos besoins et vous proposer des solutions sur mesure.</p>
    </div>
    <div class="adv" style="top:232px">
      <span class="adv__icon"><svg width="10" height="10" viewBox="0 0 10 10"><circle cx="5" cy="3" r="2" fill="#fff"/><path d="M1.5,9.5 C1.5,6 8.5,6 8.5,9.5 Z" fill="#fff"/></svg></span>
      <p class="adv__title">Un atout unique :</p>
      <p class="adv__text">Malgré mon handicap en fauteuil roulant, je suis totalement opérationnel et mon expérience me permet de vous offrir une expertise de haut niveau. Je suis disponible à 35% dès septembre 2024 et je suis prêt à mettre mon expertise et mon dynamisme au service de votre succès.</p>
    </div>
    <div class="adv adv--tint" style="top:296px">
      <p class="adv__title">N'hésitez pas à me contacter pour discuter de vos besoins et découvrir comment je peux vous aider à atteindre vos objectifs.</p>
    </div>

    <div class="mark band-mark"></div>
    <p class="block band-name">Rémi Marchand</p>
    <p class="block band-role">Assistant de projet indépendant</p>
  </section>

</main>
</body>
</html>
```